RTV Business Card

We need a new design for our business cards. We are brokers in the scrap metal industry and wants something nice, clean and very professional.

Industry/Entity Type

Business

Requirements
Must have
• Our logo
• Would probably be good to incorporate colors from logo into design.
• Example info we need on the cards.
• Name
• Company Address
• Cell Phone
• Office Phone
• Fax
• Email
• Company Website
Should not have
• Should not be too cluttered. Needs to be nice, clean and professional looking.

```html
<!DOCTYPE html>
<html lang="en">
<head>
<meta charset="utf-8">
<title>RTV Business Card</title>
<link href="https://fonts.googleapis.com/css2?family=Barlow:wght@300;400&family=Barlow+Condensed:wght@600&display=swap" rel="stylesheet">
<style>
  :root {
    --backdrop: #e4e6e8;
    --card-white: #f1f2f3;
    --ink-dark: #2a2d31;
    --brand-navy: #1d3f66;
    --brand-blue: #1f6fa8;
    --band-dark: #123a5e;
    --back-deep: #0b2f52;
    --back-light: #0f6aa3;
    --back-text: #d4e6f4;
    --back-mark: #16527f;
    --dot: #3c8ac6;
  }
  * { margin: 0; padding: 0; box-sizing: border-box; }
  html, body { width: 1200px; height: 900px; overflow: hidden; }
  body {
    background: var(--backdrop);
    display: flex;
    flex-direction: column;
    align-items: center;
    justify-content: center;
    gap: 60px;
    font-family: "Barlow", Arial, sans-serif;
  }
  .card {
    width: 630px;
    height: 360px;
    position: relative;
    overflow: hidden;
    box-shadow: 0 6px 18px rgba(0,0,0,0.18);
  }

  /* Front */
  .card-front { background: var(--card-white); }
  .brand {
    position: absolute;
    left: 110px;
    top: 50%;
    transform: translateY(-50%);
    display: flex;
    flex-direction: column;
    align-items: center;
    gap: 10px;
  }
  .brand-mark {
    font-family: "Barlow Condensed", Arial, sans-serif;
    font-weight: 600;
    font-size: 96px;
    line-height: 1;
    color: var(--brand-navy);
    letter-spacing: 4px;
  }
  .brand-name {
    font-family: "Barlow Condensed", Arial, sans-serif;
    font-weight: 600;
    font-size: 40px;
    color: var(--ink-dark);
    letter-spacing: 0.5px;
  }
  .web-band {
    position: absolute;
    top: 0;
    right: 52px;
    width: 36px;
    height: 100%;
    background: var(--brand-blue);
  }
  .web-band::after {
    content: "";
    position: absolute;
    left: 0;
    bottom: 0;
    width: 100%;
    height: 30px;
    background: var(--band-dark);
  }
  .web-band-text {
    position: absolute;
    left: 50%;
    top: 50%;
    transform: translate(-50%, -50%) rotate(-90deg);
    white-space: nowrap;
    font-size: 15px;
    color: #fff;
    letter-spacing: 0.5px;
  }

  /* Back */
  .card-back {
    background: linear-gradient(120deg, var(--back-deep) 0%, var(--back-light) 100%);
    color: var(--back-text);
    text-align: center;
  }
  .back-mark {
    position: absolute;
    left: 28px;
    top: 18px;
    font-family: "Barlow Condensed", Arial, sans-serif;
    font-weight: 600;
    font-size: 60px;
    color: var(--back-mark);
    letter-spacing: 2px;
  }
  .contact {
    position: absolute;
    left: 0;
    right: 0;
    top: 22px;
    display: flex;
    flex-direction: column;
    align-items: center;
    font-weight: 300;
    font-size: 14px;
    line-height: 1.3;
    letter-spacing: 0.5px;
  }
  .person-name { font-size: 21px; font-weight: 400; letter-spacing: 1px; }
  .person-role { font-size: 13px; margin: 0 0 10px 90px; }
  .label { font-size: 12px; letter-spacing: 1px; }
  .dot {
    width: 5px; height: 5px; border-radius: 50%;
    background: var(--dot);
    margin: 4px 0;
  }
  .address { margin-top: 14px; }
  .website { margin-top: 8px; font-size: 15px; }
</style>
</head>
<body>
  <section class="card card-front">
    <div class="brand">
      <div class="brand-mark">RTV</div>
      <div class="brand-name">Rivet Trade Ventures</div>
    </div>
    <div class="web-band"><span class="web-band-text">www.rivettradeventures.com</span></div>
  </section>

  <section class="card card-back">
    <div class="back-mark">RTV</div>
    <div class="contact">
      <div class="person-name">DANA WHITFIELD</div>
      <div class="person-role">Director</div>
      <div class="label">PHONE</div>
      <div>(555) 210-4471</div>
      <div class="dot"></div>
      <div class="label">FAX</div>
      <div>(555) 210-4472</div>
      <div class="dot"></div>
      <div class="label">EMAIL</div>
      <div>info@rivettradeventures.com</div>
      <div class="dot"></div>
      <div class="address">1240 Harbor Ridge Rd.<br>Millbrook, SC 29000</div>
      <div class="website">www.rivettradeventures.com</div>
    </div>
  </section>
</body>
</html>
```